Laundromat washing machine soap instructions poster

I own a laundromat and need a poster explaining to my customers how to load the soap, bleach and fabric softener into our washing machines. I tried to make a poster on canva but it looks terrible. My Laundromat is called "Suds Harbor" and would like my logo to also be on the poster for branding. I would like the poster to use my blue logo colors to match my brand identity.
Under the photo please include the following text:
" *Please place pods inside the washer"
Thanks
Laundromat

```html
<!DOCTYPE html>
<html lang="en">
<head>
<meta charset="utf-8">
<title>Suds Harbor – Where Does the Soap Go?</title>
<link rel="stylesheet" href="https://fonts.googleapis.com/css2?family=Poppins:wght@600;700;800&display=swap">
<style>
  :root {
    --page-bg: #e9e9e9;
    --ink: #111111;
    --brand-blue: #2f75b8;
    --sky-top: #ffffff;
    --sky-mid: #d4e9f8;
    --water-light: #6fc0ee;
    --water-mid: #2a86d8;
    --water-deep: #0b36a3;
    --arrow-red: #e0181b;
    --photo-dark: #6d6f72;
    --photo-light: #d9dadb;
    --white: #ffffff;
  }
  * { margin: 0; padding: 0; box-sizing: border-box; }
  html, body {
    width: 1200px; height: 1200px; overflow: hidden;
    background: var(--page-bg);
    font-family: "Poppins", sans-serif;
  }
  .poster {
    position: absolute; left: 170px; top: 44px;
    width: 860px; height: 1113px; overflow: hidden;
    background: linear-gradient(180deg, var(--sky-top) 0%, var(--sky-top) 32%, var(--sky-mid) 62%, #bfe0f6 75%);
  }
  .brand {
    position: absolute; top: 92px; left: 0; width: 100%;
    display: flex; justify-content: center; align-items: center; gap: 12px;
  }
  .brand-dot { width: 22px; height: 22px; border-radius: 50%; background: var(--brand-blue); }
  .brand-name {
    font-weight: 800; font-size: 44px; color: var(--brand-blue); letter-spacing: 1px;
  }
  .headline {
    position: absolute; top: 192px; left: 0; width: 100%;
    text-align: center; font-weight: 800; line-height: 1;
  }
  .headline-top { display: block; font-size: 74px; color: var(--ink); letter-spacing: -1px; }
  .headline-accent { display: block; font-size: 94px; color: var(--brand-blue); margin-top: -2px; letter-spacing: -1px; }
  .dispenser-photo {
    position: absolute; left: 237px; top: 361px; width: 398px; height: 502px;
    background: linear-gradient(180deg, var(--photo-dark) 0%, #8a8c8f 48%, var(--photo-light) 62%, var(--photo-dark) 100%);
    border-radius: 4px;
  }
  .water {
    position: absolute; left: 0; top: 790px; width: 860px; height: 323px;
  }
  .label {
    position: absolute; font-weight: 700; font-size: 32px; line-height: 1.05; color: var(--ink);
  }
  .label-left { text-align: right; right: 640px; }
  .label-right { text-align: left; left: 629px; }
  .icon-badge {
    position: absolute; width: 40px; height: 40px; border-radius: 50%;
    background: var(--white); border: 3px solid var(--brand-blue);
  }
  .arrows { position: absolute; left: 0; top: 0; width: 860px; height: 1113px; }
  .pods-note {
    position: absolute; top: 1008px; left: 0; width: 100%; text-align: center;
    font-weight: 700; font-size: 24px; letter-spacing: 2.5px; color: var(--white);
  }
</style>
</head>
<body>
  <main class="poster">
    <div class="brand">
      <span class="brand-dot"></span>
      <span class="brand-name">Suds Harbor</span>
    </div>

    <h1 class="headline">
      <span class="headline-top">WHERE DOES THE</span>
      <span class="headline-accent">SOAP GO?</span>
    </h1>

    <div class="dispenser-photo" role="img" aria-label="Photo of an open grey washing machine soap dispenser drawer with four white compartments"></div>

    <svg class="water" viewBox="0 0 860 323" role="img" aria-label="Blue water wave with bubbles filling the bottom of the poster">
      <defs>
        <linearGradient id="waterFill" x1="0" y1="0" x2="0" y2="1">
          <stop offset="0" stop-color="var(--water-light)"/>
          <stop offset="0.35" stop-color="var(--water-mid)"/>
          <stop offset="1" stop-color="var(--water-deep)"/>
        </linearGradient>
      </defs>
      <path d="M0 40 C120 0 220 70 330 50 C440 30 520 80 640 45 C730 20 800 10 860 0 L860 323 L0 323 Z" fill="url(#waterFill)"/>
    </svg>

    <div class="label label-left" style="top:620px;">Fabric<br>Softener</div>
    <div class="label label-left" style="top:734px;">Detergent</div>
    <div class="label label-right" style="top:636px;">Bleach</div>
    <div class="label label-right" style="top:730px;">Detergent</div>

    <span class="icon-badge" style="left:232px; top:638px;"></span>
    <span class="icon-badge" style="left:232px; top:733px;"></span>
    <span class="icon-badge" style="left:574px; top:638px;"></span>
    <span class="icon-badge" style="left:574px; top:733px;"></span>

    <svg class="arrows" viewBox="0 0 860 1113" aria-hidden="true">
      <defs>
        <marker id="arrowHead" viewBox="0 0 10 10" refX="5" refY="5" markerWidth="4" markerHeight="4" orient="auto">
          <path d="M0 0 L10 5 L0 10 Z" fill="var(--arrow-red)"/>
        </marker>
      </defs>
      <g fill="none" stroke="var(--arrow-red)" stroke-width="5" stroke-linecap="round" marker-end="url(#arrowHead)">
        <path d="M277 661 Q325 655 338 700"/>
        <path d="M277 755 Q312 752 318 794"/>
        <path d="M571 661 Q525 660 506 703"/>
        <path d="M571 755 Q535 755 523 794"/>
      </g>
    </svg>

    <p class="pods-note">*Please place pods inside the washer</p>
  </main>
</body>
</html>
```